New LGBT Nightclub Crowdfunding Poster

We need it to read well for social media posts. All colors should look similar to Seattle’s Sports Teams color schemes.

The top should have: The logo prominently with the fans in the background photo. and then still center and important, "Coming soon!" "You can be part of the first in line for the amazing things happening". (The call to action is the purchase of these amazing deals for the first weekend open / passes. That should be clear).

```html
<!DOCTYPE html>
<html lang="en">
<head>
<meta charset="utf-8">
<title>The Encore Eastside – Crowdfunding Levels</title>
<link rel="stylesheet" href="https://fonts.googleapis.com/css2?family=Bebas+Neue&family=Oswald:wght@500&family=Source+Sans+3:ital,wght@0,400;0,700;1,700&display=swap">
<style>
  :root {
    --navy: #1c2550;
    --navy-deep: #14183a;
    --magenta: #e0479e;
    --pink: #f08acb;
    --violet: #7a4fb5;
    --blush: #f6d9e4;
    --white: #ffffff;
    --ink: #1f2540;
  }
  * { box-sizing: border-box; margin: 0; padding: 0; }
  html, body { width: 1200px; height: 1106px; overflow: hidden; background: var(--white); }
  .poster {
    position: relative;
    width: 1200px;
    height: 1106px;
    background: var(--white);
    font-family: "Source Sans 3", Arial, sans-serif;
    color: var(--ink);
    overflow: hidden;
  }
  .crowd-photo {
    position: absolute;
    left: 0; top: 0;
    width: 1200px; height: 840px;
    background:
      radial-gradient(circle at 50% 45%, rgba(255,255,255,0.35), transparent 35%),
      radial-gradient(circle at 15% 40%, rgba(240,138,203,0.8), transparent 40%),
      radial-gradient(circle at 85% 45%, rgba(224,71,158,0.8), transparent 40%),
      linear-gradient(180deg, #2a2f6a 0%, #4a4391 22%, var(--violet) 40%, var(--magenta) 62%, #b23a8f 80%, #3c2f6e 100%);
  }
  .brand {
    position: absolute;
    left: 0; top: 300px;
    width: 1200px;
    text-align: center;
  }
  .brand-mark {
    display: inline-block;
    width: 22px; height: 22px;
    border-radius: 50%;
    background: var(--blush);
    margin-bottom: 14px;
  }
  .brand-name {
    font-family: "Oswald", sans-serif;
    font-weight: 500;
    font-size: 78px;
    line-height: 1.05;
    letter-spacing: 4px;
    color: var(--blush);
    text-transform: uppercase;
  }
  .headline {
    position: absolute;
    left: 0; top: 650px;
    width: 1050px;
    text-align: center;
    font-family: "Bebas Neue", sans-serif;
    font-size: 84px;
    line-height: 1;
    color: var(--white);
  }
  .cta-pill {
    position: absolute;
    left: 135px; top: 752px;
    width: 762px; height: 60px;
    border-radius: 30px;
    background: var(--navy);
    border: 2px solid rgba(255,255,255,0.7);
    display: flex; align-items: center; justify-content: center;
    font-family: "Bebas Neue", sans-serif;
    font-size: 27px;
    letter-spacing: 0.5px;
    color: var(--white);
  }
  .levels-title {
    position: absolute;
    left: 0; top: 840px;
    width: 1040px;
    text-align: center;
    font-weight: 700;
    font-size: 32px;
    letter-spacing: 1px;
    color: var(--navy);
  }
  .levels {
    position: absolute;
    top: 900px; left: 0;
    width: 1200px;
  }
  .level-column {
    position: absolute;
    list-style: none;
    font-size: 15px;
    line-height: 1.3;
    color: var(--ink);
  }
  .level-column li { margin-bottom: 16px; padding-left: 12px; position: relative; }
  .level-column li::before { content: "•"; position: absolute; left: 0; }
  .col-one { left: 68px; width: 270px; top: 0; }
  .col-two { left: 400px; width: 280px; top: 0; }
  .col-three { left: 700px; width: 270px; top: -16px; }
  .elite-note {
    position: absolute;
    left: 68px; top: 1092px;
    font-size: 14px; font-weight: 700; font-style: italic;
    color: var(--navy);
  }
</style>
</head>
<body>
  <main class="poster">
    <div class="crowd-photo" role="img" aria-label="Photo of a cheering crowd in silhouette with raised hands under pink and violet stage lights"></div>

    <div class="brand">
      <span class="brand-mark"></span>
      <div class="brand-name">The Encore<br>Eastside</div>
    </div>

    <h1 class="headline">Coming Soon!</h1>
    <div class="cta-pill">You can be part of the first in line for the amazing things happening</div>

    <h2 class="levels-title">CROWDFUNDING LEVELS</h2>

    <section class="levels">
      <ul class="level-column col-one">
        <li>$25 Opening Fri or Sat night Velvet GA Ticket w/Stage Royale Star. M (only 100 Available Per Night)</li>
        <li>$50 Opening Fri or Sat Night Velvet Third Tier Seating<br>(Only 60 Available Per Night)</li>
      </ul>
      <ul class="level-column col-two">
        <li>$75 Opening Fri or Sat Night Velvet Middle Tier seating Ticket w/secret Stage Royale Star.<br>(Only 60 Available Per Night)</li>
        <li>$100 Opening Fri or Sat Night Velvet VIP Ticket w/secret Stage Royale Star.<br>(Only 60 Available Per Night)</li>
      </ul>
      <ul class="level-column col-three">
        <li>$500 The Encore Pass Skip the line and free cover for 6 months. Not including Brunch Shows and Special Events. Plus The Encore Merch (50 Available)</li>
        <li>$1,000 The Encore Gold Pass. Skip the line and free cover for the year. Not including Brunch Shows and Special Events Plus The Encore Merch.<br>(100 Available)</li>
      </ul>
    </section>

    <p class="elite-note">*Ask about The Encore Elite Pass</p>
  </main>
</body>
</html>
```